Designing a Mailer/Courier bag with our Company Logo for Product Shipping

We need a quirky Mailer/Courier Bag for our company, Bijou Lavelle. As a luxury French, vintage-inspired fashion brand, we take pride in the presentation of our products, and we believe that a stylish and branded packing satchel will enhance our customers' experience.

We are looking for a design that incorporates our company logo, ‘Bijou Lavelle’ while being very feminine and French-inspired. The satchel should be practical, with a section (10.4cm x 16.5cm) for the shipping label to be placed onto the bag without it covering any logos. We are open to different colours, and designs, as long as they align with our brand image.

The packing satchel will be used to ship our products to customers worldwide, so we need a versatile design that can accommodate different-sized packing satchels.

To gain further inspiration on what type of brand Bijou Lavelle is please visit our website https://bijoulavelle.com/.

Some ideas I have attached in the images below:
- Quirky
- Looks like old mail
- Has a feel-good written phrase on the back of the packaging
- Looks vintage and unique

```html
<!DOCTYPE html>
<html lang="en">
<head>
<meta charset="utf-8">
<title>Bijou Lavelle Mailer Bag</title>
<link rel="stylesheet" href="https://fonts.googleapis.com/css2?family=Almendra+SC&family=Montserrat:wght@700;800&display=swap">
<style>
  :root {
    --paper: #c4bba6;
    --paper-light: #d8d0bd;
    --paper-dark: #a79d86;
    --sepia-deep: #8c8270;
    --sepia-mid: #9f957f;
    --ink: #231f20;
    --rule: #3d3839;
    --white: #ffffff;
    --stamp-fill: #dfc6ab;
  }
  html, body {
    margin: 0;
    padding: 0;
    overflow: hidden;
    background: var(--white);
  }
  .mailer {
    position: relative;
    width: 756px;
    height: 1200px;
    overflow: hidden;
    background: var(--paper);
  }
  .hero-photo {
    position: absolute;
    left: 0;
    top: 0;
    width: 756px;
    height: 820px;
    background:
      radial-gradient(ellipse 170px 260px at 250px 420px, rgba(140,130,112,0.75) 0%, rgba(140,130,112,0) 100%),
      radial-gradient(ellipse 150px 250px at 530px 370px, rgba(159,149,127,0.55) 0%, rgba(159,149,127,0) 100%),
      radial-gradient(ellipse 80px 110px at 225px 170px, rgba(150,138,118,0.45) 0%, rgba(150,138,118,0) 100%),
      linear-gradient(90deg, var(--paper-dark) 0%, var(--paper) 14%, var(--paper-light) 50%, var(--paper) 86%, var(--paper-dark) 100%);
  }
  .mailer-art {
    position: absolute;
    inset: 0;
  }
  .brand-name {
    font-family: "Almendra SC", serif;
    font-size: 84px;
    fill: var(--white);
  }
  .address-label {
    position: absolute;
    left: 88px;
    top: 876px;
    width: 580px;
  }
  .address-label__title {
    font-family: "Montserrat", sans-serif;
    font-weight: 800;
    font-size: 11px;
    color: var(--white);
    margin: 0;
    letter-spacing: 0.5px;
  }
  .address-label__line {
    position: absolute;
    left: 0;
    width: 580px;
    height: 1px;
    background: var(--rule);
  }
  .product-code {
    position: absolute;
    right: 28px;
    top: 1162px;
    font-family: "Montserrat", sans-serif;
    font-weight: 800;
    font-size: 13px;
    color: var(--white);
    margin: 0;
  }
</style>
</head>
<body>
<main class="mailer">
  <div class="hero-photo" role="img" aria-label="Sepia-toned vintage photograph of a woman in glasses and a floral blouse beside an old railway timetable board, overlaid with faded newspaper print"></div>

  <svg class="mailer-art" width="756" height="1200" viewBox="0 0 756 1200">
    <g class="postage-stamp">
      <rect x="551" y="42" width="137" height="93" fill="var(--white)"/>
      <g fill="var(--paper)">
        <circle cx="551" cy="50" r="3"/><circle cx="551" cy="60" r="3"/><circle cx="551" cy="70" r="3"/><circle cx="551" cy="80" r="3"/><circle cx="551" cy="90" r="3"/><circle cx="551" cy="100" r="3"/><circle cx="551" cy="110" r="3"/><circle cx="551" cy="120" r="3"/><circle cx="551" cy="130" r="3"/>
        <circle cx="688" cy="50" r="3"/><circle cx="688" cy="60" r="3"/><circle cx="688" cy="70" r="3"/><circle cx="688" cy="80" r="3"/><circle cx="688" cy="90" r="3"/><circle cx="688" cy="100" r="3"/><circle cx="688" cy="110" r="3"/><circle cx="688" cy="120" r="3"/><circle cx="688" cy="130" r="3"/>
        <circle cx="560" cy="42" r="3"/><circle cx="570" cy="42" r="3"/><circle cx="580" cy="42" r="3"/><circle cx="590" cy="42" r="3"/><circle cx="600" cy="42" r="3"/><circle cx="610" cy="42" r="3"/><circle cx="620" cy="42" r="3"/><circle cx="630" cy="42" r="3"/><circle cx="640" cy="42" r="3"/><circle cx="650" cy="42" r="3"/><circle cx="660" cy="42" r="3"/><circle cx="670" cy="42" r="3"/><circle cx="680" cy="42" r="3"/>
        <circle cx="560" cy="135" r="3"/><circle cx="570" cy="135" r="3"/><circle cx="580" cy="135" r="3"/><circle cx="590" cy="135" r="3"/><circle cx="600" cy="135" r="3"/><circle cx="610" cy="135" r="3"/><circle cx="620" cy="135" r="3"/><circle cx="630" cy="135" r="3"/><circle cx="640" cy="135" r="3"/><circle cx="650" cy="135" r="3"/><circle cx="660" cy="135" r="3"/><circle cx="670" cy="135" r="3"/><circle cx="680" cy="135" r="3"/>
      </g>
      <rect x="557" y="48" width="125" height="81" fill="var(--stamp-fill)"/>
    </g>

    <path class="label-panel" d="M0,790 Q378,473 756,800 L756,1200 L0,1200 Z" fill="var(--ink)"/>

    <path id="brand-arc" d="M70,785 Q380,622 692,818" fill="none"/>
    <text class="brand-name" text-anchor="middle">
      <textPath href="#brand-arc" startOffset="50%" textLength="640" lengthAdjust="spacing">Bijou Lavelle</textPath>
    </text>
  </svg>

  <section class="address-label">
    <p class="address-label__title">TO:</p>
    <div class="address-label__line" style="top:50px"></div>
    <div class="address-label__line" style="top:110px"></div>
    <div class="address-label__line" style="top:169px"></div>
    <div class="address-label__line" style="top:229px"></div>
  </section>

  <p class="product-code">C58</p>
</main>
</body>
</html>
```